Gin, artisan, label for Ashcombe Wine Merchants England

Product is artisan gin. Client is England’s no1 independent wine merchant chain based in Cambridge.

The pen/pencil sketches are my ideas for the main gin label - this is basically the style I want. The sketch of the round logo with shooting star is also part of this design brief - the round logo will be on the box, packaging and back label

Asymmetric, Victorian English. Monochrome/etching. Medicine bottle.
Somewhat hipster, Pallow & Pallow style. Matches aspects of Dunmere University and Cambridge City. Like a Victorian book frontispiece. The ‘bridge’ at the top is Arch of Lanterns St Oswin’s College Cambridge.

The feel should be hand-drawn / old print/etching. If necessary i can supply hand-drawn artwork for the bunches of grapes, the bridge etc.

Bottle is rectangular. Look up ‘quiet fern gin’ – same bottle. SIze of the glass where the main label will sit is 7.5 x 4 inches.

A premium gin selling at 35 pounds. Cambridge theme is important, tourists and visitors want to buy it. However, it is a serious artisan gin not a gimmick

• the upper "Ashcombe WIne Merhants" part needs to be separated from the word "GIN", by the scroll and by being in a different font. This is because 'Wexmoor Gin' is a trademark registrered by someone else. Ashcombe WIne Merhants as a gin brand is registered by us already.
• the banner / scroll should look like it is running off the main label and onto the border.

```html
<!DOCTYPE html>
<html lang="en">
<head>
<meta charset="utf-8">
<title>Ashcombe Wine Marchants – Artisan London Dry Gin Label</title>
<link rel="stylesheet" href="https://fonts.googleapis.com/css2?family=Oswald:wght@400;500;600;700&family=Rye&family=Bungee+Shade&display=swap">
<style>
  :root {
    --backdrop: #e6e5e2;
    --label-light: #fbfbfb;
    --label-silver: #dcdcdc;
    --ink: #1d1d1d;
    --ink-soft: #555555;
    --paper: #ffffff;
    --etching-light: #cfcfcf;
    --etching-dark: #6d6d6d;
  }
  * { margin: 0; padding: 0; box-sizing: border-box; }
  html, body {
    width: 930px; height: 1200px; overflow: hidden;
    background: var(--backdrop);
  }
  .canvas { position: relative; width: 930px; height: 1200px; }

  .gin-label {
    position: absolute; left: 175px; top: 30px;
    width: 580px; height: 1140px;
    border-radius: 26px;
    background: radial-gradient(ellipse at 50% 45%, var(--label-light) 0%, var(--label-light) 55%, var(--label-silver) 100%);
    color: var(--ink);
    overflow: hidden;
  }
  .label-art { position: absolute; inset: 0; width: 580px; height: 1140px; }

  .label-text {
    position: absolute; left: 0; width: 100%;
    text-align: center; white-space: nowrap;
    font-family: 'Oswald', sans-serif;
  }
  .motto { top: 82px; font-size: 40px; font-weight: 400; letter-spacing: 3px; }
  .motto .star { font-size: 22px; vertical-align: 6px; margin: 0 4px; }

  .brand-name {
    top: 300px; font-size: 104px; font-weight: 600; letter-spacing: 1px; line-height: 1;
    transform: scaleX(0.86);
  }
  .brand-subtitle { top: 420px; font-size: 40px; font-weight: 500; letter-spacing: 1px; line-height: 1; }

  .banner-text {
    top: 522px; font-size: 36px; font-weight: 500; color: var(--paper);
    letter-spacing: 1px; transform: rotate(-6deg);
  }
  .presents { top: 636px; font-size: 22px; font-weight: 600; letter-spacing: 0.5px; }
  .gin-style { top: 680px; font-family: 'Rye', serif; font-size: 30px; letter-spacing: 0.5px; }
  .gin-style .star { font-family: 'Oswald', sans-serif; font-size: 24px; margin: 0 6px; vertical-align: 3px; }

  .gin-word {
    top: 757px; height: 146px;
    display: flex; justify-content: center; align-items: center;
  }
  .gin-word span {
    display: inline-block; padding: 0 14px;
    font-family: 'Bungee Shade', sans-serif; font-size: 118px; line-height: 1;
    background: var(--label-light);
  }

  .strength, .volume { top: 922px; width: auto; font-size: 42px; font-weight: 400; }
  .strength { left: 60px; }
  .volume { left: auto; right: 60px; }
  .volume sup { font-size: 18px; vertical-align: 18px; }
  .origin { top: 928px; font-size: 18px; font-weight: 500; letter-spacing: 0.5px; }
</style>
</head>
<body>
<main class="canvas">
  <section class="gin-label" aria-label="Gin bottle label">
    <svg class="label-art" viewBox="0 0 580 1140">
      <defs>
        <linearGradient id="bridge-etching" x1="0" y1="0" x2="0" y2="1">
          <stop offset="0" stop-color="var(--etching-dark)"/>
          <stop offset="0.6" stop-color="var(--etching-light)"/>
          <stop offset="1" stop-color="var(--label-light)"/>
        </linearGradient>
        <radialGradient id="grapes-etching">
          <stop offset="0" stop-color="var(--etching-dark)"/>
          <stop offset="1" stop-color="var(--etching-light)"/>
        </radialGradient>
        <pattern id="engraved-lines" width="6" height="6" patternUnits="userSpaceOnUse">
          <line x1="0" y1="1" x2="6" y2="1" stroke="var(--ink-soft)" stroke-width="1.4"/>
        </pattern>
      </defs>

      <path class="frame-outer" d="M30 60 H200 Q210 20 250 18 H330 Q370 20 380 60 H550 V1080 H380 Q370 1115 330 1120 H250 Q210 1115 200 1080 H30 Z"
            fill="none" stroke="var(--ink)" stroke-width="4"/>
      <path class="frame-inner" d="M42 72 H208 Q220 32 252 30 H328 Q360 32 372 72 H538 V1068 H372 Q360 1102 328 1108 H252 Q220 1102 208 1068 H42 Z"
            fill="none" stroke="var(--ink)" stroke-width="1.5"/>

      <g class="corner-studs" fill="var(--label-light)" stroke="var(--ink)" stroke-width="3">
        <circle cx="30" cy="60" r="11"/><circle cx="550" cy="60" r="11"/>
        <circle cx="30" cy="1080" r="11"/><circle cx="550" cy="1080" r="11"/>
      </g>
      <g fill="var(--ink)">
        <circle cx="30" cy="60" r="4"/><circle cx="550" cy="60" r="4"/>
        <circle cx="30" cy="1080" r="4"/><circle cx="550" cy="1080" r="4"/>
      </g>

      <rect class="crest-ornament" x="232" y="38" width="116" height="28" rx="6" fill="var(--etching-light)"
            role="img" aria-label="Engraved flourish ornament"/>

      <line x1="60" y1="150" x2="520" y2="150" stroke="var(--ink)" stroke-width="2"/>

      <rect class="bridge-etching" x="56" y="160" width="468" height="130" fill="url(#bridge-etching)"
            stroke="var(--ink)" stroke-width="2"
            role="img" aria-label="Etching of the Arch of Lanterns at St Oswin’s College"/>

      <g class="ribbon" transform="rotate(-6 290 545)">
        <path d="M-10 530 L40 520 L40 585 L-10 595 L15 560 Z" fill="var(--ink)"/>
        <path d="M590 505 L540 500 L540 565 L590 570 L565 538 Z" fill="var(--ink)"/>
        <rect x="40" y="510" width="500" height="66" fill="var(--ink)"/>
        <line x1="48" y1="516" x2="532" y2="516" stroke="var(--paper)" stroke-width="1.2"/>
        <line x1="48" y1="570" x2="532" y2="570" stroke="var(--paper)" stroke-width="1.2"/>
      </g>

      <line x1="180" y1="628" x2="400" y2="628" stroke="var(--ink)" stroke-width="1.5"/>
      <line x1="56" y1="672" x2="524" y2="672" stroke="var(--ink)" stroke-width="2"/>
      <line x1="56" y1="728" x2="524" y2="728" stroke="var(--ink)" stroke-width="2"/>

      <rect x="56" y="745" width="468" height="160" fill="url(#engraved-lines)"/>
      <rect x="56" y="745" width="468" height="160" fill="none" stroke="var(--ink)" stroke-width="2"/>

      <line x1="56" y1="915" x2="524" y2="915" stroke="var(--ink)" stroke-width="2"/>
      <line x1="56" y1="985" x2="524" y2="985" stroke="var(--ink)" stroke-width="2"/>

      <circle class="grapes-etching" cx="290" cy="1048" r="52" fill="url(#grapes-etching)" stroke="var(--ink)" stroke-width="2"
              role="img" aria-label="Engraved bunch of grapes"/>
    </svg>

    <p class="label-text motto">VENI<span class="star">★</span>VIDI<span class="star">★</span>BIBI</p>
    <h1 class="label-text brand-name">ASHCOMBE</h1>
    <p class="label-text brand-subtitle">WINE MARCHANTS</p>
    <p class="label-text banner-text">EST 1093 BEST IN BRITAIN</p>
    <p class="label-text presents">PRESENT TO YOU THEIR FINEST</p>
    <p class="label-text gin-style">ARTISAN<span class="star">★</span>LONDONDRY</p>
    <h2 class="label-text gin-word"><span>GIN</span></h2>
    <p class="label-text strength">40%</p>
    <p class="label-text origin">MADE IN ENGLAND</p>
    <p class="label-text volume">70<sup>CL</sup></p>
  </section>
</main>
</body>
</html>
```